Professional Business Card - TWO SIDES

I need a new business card design to be used by myself and my employees. I would like a professional card and for the front I thought I would like a dark blue thatch with our logo in a raised gold foil on top of it. On the other side I would like name, position, and contact info. I've uploaded our old design for an example of the info used.

Target Market(s)

Business Clients

Industry/Entity Type

CPA Firm

Contact Information for Business Card

Logo, Name, Title, Address, Phone Numbers, Website address, Email Address

Font styles to use
Serif
Sans Serif

Colors
0054AA
0677BA
7BADD7
CADEEF
E8F1F8
0094D4
00A9DD
6FCCEA
C7EBF8
E9F6FB

Requirements
Must have
• Modern Professional Look
Nice to have
• Logo in Gold Foil or ability to have is raised. I like our logo in a single color
Should not have
• I've uploaded old business card

```html
<!DOCTYPE html>
<html lang="en">
<head>
<meta charset="utf-8">
<title>Hale &amp; Hale Business Card</title>
<link href="https://fonts.googleapis.com/css2?family=Montserrat:wght@400;500;600;700&display=swap" rel="stylesheet">
<style>
  :root {
    --backdrop: #3b322e;
    --navy: #0d3b63;
    --navy-deep: #0a2f52;
    --gold: #d9ad3c;
    --paper: #f7f8f8;
    --ink: #17365f;
    --text-grey: #55595e;
    --rule: #c9ccd0;
    --band-dark: #15386a;
    --band-blue: #0677ba;
  }
  * { margin: 0; padding: 0; box-sizing: border-box; }
  html, body {
    width: 1200px; height: 848px; overflow: hidden;
    background: var(--backdrop);
    font-family: "Montserrat", sans-serif;
  }
  .canvas {
    position: relative; width: 1200px; height: 848px;
    display: flex; align-items: center; justify-content: center; gap: 60px;
  }
  .card {
    position: relative; width: 520px; height: 297px;
    border-radius: 4px; overflow: hidden;
    box-shadow: 0 14px 30px rgba(0,0,0,0.35);
  }
  .card-front {
    background: var(--navy);
    display: flex; flex-direction: column; align-items: center; justify-content: center;
  }
  .brand-name {
    font-weight: 700; letter-spacing: 1px; text-transform: uppercase; line-height: 1;
  }
  .brand-tagline {
    font-weight: 600; text-transform: uppercase; letter-spacing: 3px; line-height: 1;
  }
  .card-front .brand-name { color: var(--gold); font-size: 52px; }
  .card-front .brand-tagline { color: var(--gold); font-size: 15px; margin-top: 10px; }

  .card-back { background: var(--paper); }
  .back-logo {
    position: absolute; left: 34px; top: 108px; width: 230px;
  }
  .card-back .brand-name { color: var(--ink); font-size: 31px; }
  .card-back .brand-tagline { color: var(--ink); font-size: 9.5px; letter-spacing: 1.6px; margin-top: 7px; }
  .divider {
    position: absolute; left: 290px; top: 62px; width: 1px; height: 150px; background: var(--rule);
  }
  .contact-block { position: absolute; left: 312px; top: 62px; }
  .person-name { font-size: 20px; font-weight: 700; color: var(--ink); }
  .person-title { font-size: 11px; color: var(--text-grey); margin-top: 2px; }
  .contact-list { list-style: none; margin-top: 12px; }
  .contact-list li {
    display: flex; align-items: center; gap: 8px;
    font-size: 11px; color: var(--text-grey); line-height: 17px;
  }
  .contact-list svg { width: 11px; height: 11px; flex: none; }
  .address { font-size: 11px; color: var(--text-grey); line-height: 16px; margin-top: 12px; }
  .base-band { position: absolute; left: 0; right: 0; bottom: 0; height: 10px; display: flex; }
  .base-band .band-dark { width: 52%; background: var(--band-dark); }
  .base-band .band-blue { flex: 1; background: var(--band-blue); margin-left: 3px; }
</style>
</head>
<body>
<div class="canvas">
  <section class="card card-front">
    <div class="brand-name">Hale &amp; Hale</div>
    <div class="brand-tagline">Certified Public Accountants</div>
  </section>

  <section class="card card-back">
    <div class="back-logo">
      <div class="brand-name">Hale &amp; Hale</div>
      <div class="brand-tagline">Certified Public Accountants</div>
    </div>
    <div class="divider"></div>
    <div class="contact-block">
      <div class="person-name">Daniel Hale</div>
      <div class="person-title">Managing Partner</div>
      <ul class="contact-list">
        <li>
          <svg viewBox="0 0 24 24" fill="none" stroke="#55595e" stroke-width="2.2"><path d="M5 3h4l2 5-3 2a11 11 0 0 0 6 6l2-3 5 2v4a2 2 0 0 1-2 2A17 17 0 0 1 3 5a2 2 0 0 1 2-2z"/></svg>
          555.014.2290
        </li>
        <li>
          <svg viewBox="0 0 24 24" fill="none" stroke="#55595e" stroke-width="2.2"><rect x="2" y="5" width="20" height="14" rx="1"/><path d="M2 6l10 7 10-7"/></svg>
          info@haleandhale.com
        </li>
        <li>
          <svg viewBox="0 0 24 24" fill="none" stroke="#55595e" stroke-width="2"><circle cx="12" cy="12" r="10"/><path d="M2 12h20M12 2c3 3 4 6.5 4 10s-1 7-4 10c-3-3-4-6.5-4-10s1-7 4-10z"/></svg>
          www.haleandhale.com
        </li>
      </ul>
      <div class="address">
        Harbor Boulevard<br>
        218 N Linden Street<br>
        Fairview, MS 39000
      </div>
    </div>
    <div class="base-band"><span class="band-dark"></span><span class="band-blue"></span></div>
  </section>
</div>
</body>
</html>
```